Cover design needed for scholarship book whose intended audience is students with medical conditions

I need a book cover designed for a book called, “The Thistle Grant: Ways To Change Your Health Challenge Into Open Funds For University.” This book is aimed at students with a variety of medical conditions. I wrote The Thistle Grant after I received a medical-based scholarship ($96,000) to attend college and law school based on my allergies to pollen—hence the title. However, this government program applies to just about any medical condition—not just allergies. I have assisted students in applying for this program who suffer from many different medical conditions. So I would like the cover design to convey that message—that this program applies to many different medical conditions. One of the big misconceptions about medical-based scholarships is you will only qualify if you have a really serious medical condition. So I would like to see some cover designs that list some common medical conditions in order to convey to the reader that many different medical conditions qualify. A few possible medical conditions are allergies, asthma, ADHD, depression, anxiety, back pain, eating disorders, bipolar, sleep disorders, and OCD. Possible ways to convey this may be to have the names of some of these common medical conditions written on graduation caps or randomly dispersed in the background, etc. However, this isn’t the only theme I would like to see. In essence, I give you creative liberty to wow me with your design prowess. The point of crowd design is to get variety of designs to choose from that I may not have thought of on my own. I have dabbled with some ideas that blend the themes of the education world and the medical world and I think this is the essence of the book. What ever you come up with, it needs to make it clear at a glance that this book helps you pay for college on the basis of your medical condition—whatever medical condition that may be. To see a simple mock up I did (that I don't want to use) go to healthawardfinder.example

The book is 153 pages on 5x8 paper. I am planning to print the book through PageForge, so the cover should adhere to the PageForge design requirements. I can provide the PageForge template if needed.

Updates: Please be able to provide a few updates to the cover design if your design is selected. After choosing the final design, physical proofs of the book will be ordered so I can see what your design looks like in real life. After the proofs are reviewed, I may need some minor changes (i.e., maybe the back cover text needs a new font size, etc..) Also, after I use the proofs to solicit endorsements, I am planning to purchase my own ISBN number and barcode. I would like the designer to be able to update my cover to include a new ISBN and barcode after the initial proofs are printed which should be 3-4 weeks later. So please be able to provide a few updates to the cover design if your design is selected.

Target Market(s)

Students/parents who are planning to attend college and have some type of medical condition

Industry/Entity Type

College

Font styles to use
Serif

Requirements
Must have
• My project must have a general education/medical theme
Nice to have
• I'd like to see some designs that include random medical conditions dispersed on the cover. Maybe a different medical condition written on several different graduation caps, or some other context.
Should not have
• The cover design should not depict persons with severe medical conditions--i.e., people in wheelchairs, hospital beds, etc.

```html
<!DOCTYPE html>
<html lang="en">
<head>
<meta charset="utf-8">
<title>The Thistle Grant – Book Cover</title>
<link rel="stylesheet" href="https://fonts.googleapis.com/css2?family=Tinos:wght@400;700&family=Arimo:wght@400&family=Fira+Sans+Condensed:wght@800&display=swap">
<style>
  :root {
    --sky-top: #2f86d3;
    --sky-mid: #4a9be0;
    --sky-deep: #1d6fc0;
    --cloud: rgba(255,255,255,0.55);
    --ink: #ffffff;
    --rule: rgba(255,255,255,0.9);
    --bird-a: #8a8f7a;
    --bird-b: #a33a3a;
    --photo-a: #6b7a55;
    --photo-b: #d9dde3;
  }
  * { margin: 0; padding: 0; box-sizing: border-box; }
  html, body { width: 1200px; height: 881px; overflow: hidden; background: var(--sky-deep); }
  .cover {
    position: relative; width: 1200px; height: 881px; overflow: hidden;
    color: var(--ink); font-family: "Tinos", "Times New Roman", serif;
  }
  /* back */
  .back {
    position: absolute; left: 0; top: 0; width: 620px; height: 881px;
    background: linear-gradient(180deg, #3b93dc 0%, #2a82d0 50%, #2376c6 100%);
  }
  .back-heading {
    position: absolute; left: 34px; top: 155px; width: 500px;
    text-align: center; font-weight: 700; font-size: 20px; line-height: 26px;
  }
  .rule { position: absolute; left: 34px; width: 541px; height: 2px; background: var(--rule); }
  .rule.top { top: 209px; }
  .rule.bottom { top: 673px; }
  .blurb {
    position: absolute; left: 34px; top: 222px; width: 527px;
    font-size: 15.2px; line-height: 19.3px; text-align: justify;
  }
  .author-photo {
    position: absolute; left: 34px; top: 525px; width: 149px; height: 148px;
    border: 3px solid #f3f3f3; box-shadow: 2px 3px 5px rgba(0,0,0,0.35);
    background: linear-gradient(135deg, var(--photo-a) 0%, #8f9a78 45%, var(--photo-b) 100%);
  }
  .author-bio {
    position: absolute; left: 201px; top: 532px; width: 360px;
    font-size: 15.2px; line-height: 19.3px; text-align: justify;
  }
  /* spine */
  .spine {
    position: absolute; left: 576px; top: 0; width: 44px; height: 881px;
    background: linear-gradient(90deg, #2a82d0, #2e86d3);
  }
  .spine-title, .spine-author {
    position: absolute; left: 22px; white-space: nowrap;
    transform-origin: 0 0; transform: rotate(90deg) translateY(-50%);
    font-size: 31px; letter-spacing: 0.5px;
  }
  .spine-title { top: 42px; }
  .spine-author { top: 600px; }
  /* front */
  .front {
    position: absolute; left: 620px; top: 0; width: 580px; height: 881px;
    background:
      radial-gradient(ellipse 120px 60px at 560px 80px, var(--cloud), transparent 70%),
      radial-gradient(ellipse 150px 70px at 500px 280px, var(--cloud), transparent 70%),
      radial-gradient(ellipse 130px 60px at 120px 420px, var(--cloud), transparent 70%),
      radial-gradient(ellipse 130px 55px at 480px 450px, var(--cloud), transparent 70%),
      radial-gradient(ellipse 150px 55px at 250px 530px, var(--cloud), transparent 70%),
      radial-gradient(ellipse 220px 90px at 420px 760px, rgba(255,255,255,0.45), transparent 70%),
      radial-gradient(ellipse 260px 80px at 380px 860px, rgba(255,255,255,0.5), transparent 70%),
      linear-gradient(180deg, var(--sky-top) 0%, var(--sky-mid) 55%, #5aa6e4 100%);
  }
  .front-title {
    position: absolute; left: 0; top: 28px; width: 580px; text-align: center;
    font-family: "Fira Sans Condensed", "Arial Narrow", sans-serif; font-weight: 800;
    font-size: 86px; line-height: 86px; letter-spacing: 1px;
  }
  .hero-illustration {
    position: absolute; left: 100px; top: 218px; width: 380px; height: 372px;
    border-radius: 45% 55% 50% 50%;
    background: radial-gradient(ellipse at 40% 40%, var(--bird-b) 0%, var(--bird-a) 35%, rgba(138,143,122,0) 72%);
    opacity: 0.75;
  }
  .condition {
    position: absolute; font-family: "Arimo", Arial, sans-serif; font-size: 14.5px;
    line-height: 19px; white-space: nowrap;
  }
  .condition.mood { left: 452px; top: 244px; transform: rotate(35deg); transform-origin: 0 0; }
  .condition.breath { left: 75px; top: 420px; transform: rotate(-20deg); }
  .condition.ocd { left: 462px; top: 428px; transform: rotate(-12deg); }
  .condition.rest { left: 175px; top: 500px; transform: rotate(-20deg); }
  .subtitle {
    position: absolute; left: 0; top: 636px; width: 580px; text-align: center;
    font-size: 31px; line-height: 41px;
  }
  .front-author {
    position: absolute; left: 0; top: 778px; width: 580px; text-align: center;
    font-size: 74px; line-height: 74px;
  }
</style>
</head>
<body>
<div class="cover">
  <section class="back">
    <h2 class="back-heading">How Anyone Can Get Free Money for College on the Basis of Their Medical Condition!</h2>
    <div class="rule top"></div>
    <p class="blurb">The first book ever to expose the secret world of medical-based scholarships, The Thistle Grant shows you how to turn any medical condition into free money for college! Whether your medical condition is incredibly serious or just mildly annoying, this book can save you a fortune in college expenses! Medical-based scholarships provide students with an exciting opportunity to pay for college on the basis of just about any medical condition—allergies, ADHD, anxiety, depression, back pain—the list goes on and on. But to take advantage of this program, first you need to know how to apply!<br>The Thistle Grant is a step-by-step guide that walks students and parents through the simple application process for the medical-based scholarship program. It doesn’t matter where you live, what college you plan to attend, or what medical condition you suffer from, The Thistle Grant applies to you! With the ever-increasing cost of a college education, if you suffer from any medical condition whatsoever, The Thistle Grant is a must read!</p>
    <div class="author-photo" role="img" aria-label="Portrait photo of the author outdoors"></div>
    <p class="author-bio">Daniel Marsh is an attorney–author who received $96,000 through the medical-based scholarship program on the basis of his medical conditions of asthma and pollen allergies (hence the book’s title, The Thistle Grant). Daniel is a former Assistant Attorney General for the state of Florida. Daniel is currently an Attorney–Advisor for the Federal Legal Services Bureau.</p>
    <div class="rule bottom"></div>
  </section>

  <section class="spine">
    <div class="spine-title">THE THISTLE GRANT</div>
    <div class="spine-author">DANIEL MARSH</div>
  </section>

  <section class="front">
    <h1 class="front-title">THE THISTLE<br>GRANT</h1>
    <div class="hero-illustration" role="img" aria-label="Hummingbird in flight wearing a graduation cap"></div>
    <div class="condition mood">Depression<br>&nbsp;&nbsp;Anxiety</div>
    <div class="condition breath">Allergies<br>&nbsp;&nbsp;Asthma</div>
    <div class="condition ocd">OCD<br>Back pain</div>
    <div class="condition rest">Sleep disorders<br>Eating disorders</div>
    <p class="subtitle">WAYS TO CHANGE YOUR<br>HEALTH CHALLENGE INTO<br>OPEN FUNDS FOR UNIVERSITY.</p>
    <p class="front-author">DANIEL MARSH</p>
  </section>
</div>
</body>
</html>
```